Business Card Design for Occupational Medicine Start Up Company

We need to design a professional business card. We are a healthcare company providing occupational medicine services to blue collar industries. We are professional, efficient and high quality service providers.

Target Market(s)

Blue Collar Industry: Shipbuilding, Ports, Trucking Companies; The Executives and Safety Officers for these companies

Industry/Entity Type

Healthcare

Contact Information for Business Card

Logo, Name, Title, Email, Phone

Other font styles liked:
• Please match our Brand Guide

Requirements
Must have
• Our Company Colors and Logo

```html
<!DOCTYPE html>
<html lang="en">
<head>
<meta charset="utf-8">
<title>ShiftWell Clinics – Business Card</title>
<link href="https://fonts.googleapis.com/css2?family=Montserrat:wght@400;600;800&family=Poppins:wght@500&display=swap" rel="stylesheet">
<style>
  :root {
    --navy: #2d347d;
    --sky: #27a6de;
    --amber: #f2b15a;
    --white: #ffffff;
    --backdrop: #e6e6e6;
  }
  * { margin: 0; padding: 0; box-sizing: border-box; }
  html, body {
    width: 1200px; height: 1200px; overflow: hidden;
    background: var(--backdrop);
    font-family: "Montserrat", sans-serif;
  }
  .card {
    position: absolute; left: 297px; width: 605px; height: 345px;
    overflow: hidden;
  }
  .card-front { top: 192px; background: var(--navy); }
  .card-back { top: 662px; background: var(--white); }

  .brand-mark { position: absolute; border-radius: 50%; }
  .card-front .brand-mark {
    left: 261px; top: 104px; width: 84px; height: 84px; background: var(--amber);
  }
  .card-front .brand-name {
    position: absolute; left: 0; width: 100%; top: 203px; text-align: center;
    color: var(--white); font-weight: 800; font-size: 25px; letter-spacing: 1px;
  }

  .card-back .brand-mark {
    left: 154px; top: 46px; width: 80px; height: 80px; background: var(--amber);
  }
  .card-back .brand-name {
    position: absolute; left: 252px; top: 70px;
    color: var(--navy); font-weight: 800; font-size: 22px; letter-spacing: 0.5px;
  }

  .holder { position: absolute; left: 50px; top: 210px; }
  .holder-name { color: var(--navy); font-weight: 800; font-size: 22px; line-height: 1.1; }
  .holder-title { color: var(--sky); font-weight: 400; font-size: 17px; letter-spacing: 0.5px; margin-top: 2px; }

  .divider {
    position: absolute; left: 301px; top: 196px; width: 2px; height: 73px; background: var(--amber);
  }
  .contacts {
    position: absolute; left: 327px; top: 196px; list-style: none;
    color: var(--sky); font-size: 17px; line-height: 24px; letter-spacing: 0.5px;
  }

  .stripe { position: absolute; left: 0; width: 100%; }
  .stripe-sky { top: 298px; height: 4px; background: var(--sky); }
  .stripe-amber { top: 305px; height: 4px; background: var(--amber); }
  .address-band {
    top: 312px; height: 33px; background: var(--navy);
    color: var(--white); font-family: "Poppins", sans-serif; font-weight: 500;
    font-size: 13px; text-align: center; line-height: 33px;
  }
</style>
</head>
<body>
  <section class="card card-front">
    <span class="brand-mark"></span>
    <div class="brand-name">SHIFTWELL CLINICS</div>
  </section>

  <section class="card card-back">
    <span class="brand-mark"></span>
    <div class="brand-name">SHIFTWELL CLINICS</div>

    <div class="holder">
      <div class="holder-name">DANIEL R. HOLLIS</div>
      <div class="holder-title">Chief Executive Manager</div>
    </div>

    <span class="divider"></span>

    <ul class="contacts">
      <li>+1 555-014-2290</li>
      <li>hello@shiftwellclinics.com</li>
      <li>shiftwellclinics.com</li>
    </ul>

    <span class="stripe stripe-sky"></span>
    <span class="stripe stripe-amber"></span>
    <div class="stripe address-band">735 Dockyard Way Bayport, VA 23000</div>
  </section>
</body>
</html>
```